Aesthetics Company Flyer (description of services)

We need a 5.5"x8.5" flyer describing the services we offer at velvet horizon aesthetics. We are an aesthetics company located in Conroe TX. Our products and services can be found at www.vhaesthetics-demo.com/services . We would like to see designs that are cohesive with our brand and website: https://www.vhaesthetics-demo.com/

```html
<!DOCTYPE html>
<html lang="en">
<head>
<meta charset="utf-8">
<title>Velvet Horizon Aesthetics – Services Flyer</title>
<link rel="stylesheet" href="https://fonts.googleapis.com/css2?family=Jost:wght@400;500&family=Montserrat:wght@400;500;600;800&family=Roboto+Condensed:wght@400&display=swap">
<style>
  :root {
    --lilac: #d1a9c9;
    --salmon: #fbc5b7;
    --rose-band: #f0a9a8;
    --blush: #f6e1da;
    --card: #ecc4c8;
    --ring: #e3b2c4;
    --ink: #2b2727;
    --brand-ink: #8e6f6b;
    --white: #ffffff;
  }
  * { box-sizing: border-box; margin: 0; padding: 0; }
  html, body { width: 850px; height: 1200px; overflow: hidden; background: var(--blush); }
  .flyer { position: relative; width: 850px; height: 1200px; overflow: hidden; font-family: "Montserrat", sans-serif; color: var(--ink); }
  .layer { position: absolute; left: 0; top: 0; width: 850px; height: 1200px; }

  .hero-photo { position: absolute; left: 0; top: 0; width: 640px; height: 600px;
    background: radial-gradient(ellipse at 55% 45%, #dcbcd3 0%, #c9a1c0 55%, var(--lilac) 100%); }
  .portrait { position: absolute; left: 470px; top: 26px; width: 333px; height: 520px;
    border-radius: 160px 160px 20px 20px;
    background: linear-gradient(180deg, #6b4a3a 0%, #9a6a50 35%, #f3f1f1 60%, #ffffff 100%); }

  .headline { position: absolute; left: 70px; top: 58px; font-family: "Jost", sans-serif; font-weight: 400;
    color: var(--white); text-transform: uppercase; line-height: 62px; letter-spacing: -1px; white-space: nowrap; }
  .headline .big { font-size: 63px; }
  .headline .small { font-size: 37px; }

  .contact { position: absolute; left: 25px; top: 426px; }
  .contact .phone { font-weight: 800; font-size: 46px; line-height: 46px; letter-spacing: 0.5px; }
  .contact .email { font-weight: 600; font-size: 20.5px; line-height: 22px; margin-top: 2px; }
  .contact .address { font-family: "Roboto Condensed", sans-serif; font-size: 25px; line-height: 30px; margin-top: 12px; }

  .circle-photo { position: absolute; border-radius: 50%; border: 7px solid var(--ring); }
  .circle-injection { left: 340px; top: 608px; width: 208px; height: 208px;
    background: linear-gradient(135deg, #f2f0f0 0%, #d9b9a6 45%, #c79a85 100%); }
  .circle-peel { left: 570px; top: 550px; width: 264px; height: 264px;
    background: radial-gradient(circle at 45% 40%, #f2d23a 0%, #e7c431 45%, #3a3434 100%); }

  .brand { position: absolute; left: 51px; top: 665px; width: 170px; display: flex; flex-direction: column; align-items: center; gap: 10px; }
  .brand-dot { width: 56px; height: 56px; border-radius: 50%; background: var(--ring); }
  .brand-name { font-weight: 500; font-size: 12px; letter-spacing: 2px; text-transform: uppercase; text-align: center; color: var(--brand-ink); line-height: 18px; }

  .services-title { position: absolute; left: 63px; top: 790px; font-weight: 800; font-size: 32px; line-height: 34px;
    letter-spacing: 0.3px; border-bottom: 2px solid #8e8585; white-space: nowrap; }

  .service { position: absolute; }
  .service h2 { font-weight: 500; font-size: 15.5px; line-height: 18px; letter-spacing: 0.3px; text-transform: uppercase; white-space: nowrap; }
  .service h2 small { font-size: 9px; letter-spacing: 0; }
  .service .sub { font-size: 12px; line-height: 14px; }
  .service p { background: var(--card); border-radius: 4px; font-size: 11px; line-height: 14px; padding: 7px 9px 6px 8px; }

  .svc-weight { left: 52px; top: 842px; width: 240px; }
  .svc-weight h2 { margin-left: 18px; }
  .svc-weight p { margin-top: 15px; min-height: 130px; padding-left: 18px; }

  .svc-neuro { left: 313px; top: 837px; width: 240px; }
  .svc-neuro h2, .svc-neuro .sub { margin-left: 15px; }
  .svc-neuro p { margin-top: 10px; min-height: 148px; padding-left: 15px; }

  .svc-fillers { left: 570px; top: 837px; width: 229px; }
  .svc-fillers h2 { margin-left: 7px; }
  .svc-fillers p { margin-top: 14px; min-height: 158px; }

  .svc-fgf { left: 64px; top: 1030px; width: 228px; }
  .svc-fgf p { margin-top: 4px; padding-left: 6px; }

  .svc-pen { left: 322px; top: 1035px; width: 217px; }
  .svc-pen h2 { margin-left: 8px; }
  .svc-pen p { margin-top: 0; min-height: 119px; }

  .svc-peels { left: 570px; top: 1036px; width: 218px; }
  .svc-peels h2 { margin-left: 3px; }
  .svc-peels p { margin-top: 1px; min-height: 64px; }
</style>
</head>
<body>
<main class="flyer">
  <svg class="layer" viewBox="0 0 850 1200" aria-hidden="true">
    <rect width="850" height="620" fill="var(--lilac)"/>
  </svg>
  <div class="hero-photo" role="img" aria-label="Photo of a woman receiving a facial injection treatment, tinted lilac"></div>
  <svg class="layer" viewBox="0 0 850 1200" aria-hidden="true">
    <path d="M0,312 C150,380 330,420 470,415 C620,410 740,370 850,330 L850,1200 L0,1200 Z" fill="var(--salmon)"/>
    <path d="M0,312 C140,360 300,385 470,405" fill="none" stroke="var(--rose-band)" stroke-width="4"/>
  </svg>
  <div class="portrait" role="img" aria-label="Portrait of the smiling lead practitioner in a white coat"></div>
  <svg class="layer" viewBox="0 0 850 1200" aria-hidden="true">
    <path d="M850,290 C760,420 650,500 520,560 C420,600 350,610 300,615 C430,600 560,560 660,510 C740,470 800,420 850,380 Z" fill="var(--rose-band)"/>
    <path d="M0,598 C200,605 420,590 560,545 C680,505 780,450 850,400 L850,440 C760,500 640,560 500,600 C360,640 180,648 0,646 Z" fill="var(--rose-band)"/>
    <path d="M0,646 C200,648 380,634 520,600 C660,565 770,505 850,440 L850,1200 L0,1200 Z" fill="var(--blush)"/>
  </svg>

  <h1 class="headline">
    <span class="small">We</span> <span class="big">Change</span><br>
    <span class="big">The World</span><br>
    <span class="small">One</span> <span class="big">Beautiful</span><br>
    <span class="big">Face</span> <span class="small">at a time</span>
  </h1>

  <section class="contact">
    <div class="phone">936 555 0142</div>
    <div class="email">hello@vhaesthetics-demo.com</div>
    <div class="address">1200 Sample Rd #100, Magnolia, TX 77000</div>
  </section>

  <div class="brand">
    <span class="brand-dot"></span>
    <span class="brand-name">velvet horizon aesthetics</span>
  </div>

  <div class="circle-photo circle-injection" role="img" aria-label="Close-up photo of a neurotoxin injection near the eye"></div>
  <div class="circle-photo circle-peel" role="img" aria-label="Photo of a yellow chemical peel being brushed onto a client's face"></div>

  <h2 class="services-title">OUR SERVICES</h2>

  <section class="service svc-weight">
    <h2>Weightloss</h2>
    <p>Semaglutide stimulates insulin to be released from the pancreas in an effort to slow down gastric emptying and inhibits inappropriate release of sugars after we eat. Simply put, this process ultimately reduces our food intake from within, thereby leading to weight loss.</p>
  </section>

  <section class="service svc-neuro">
    <h2>Neurotoxin</h2>
    <div class="sub">(Wrinkle Relaxer)</div>
    <p>Neurotoxin injections lessens facial lines that can give you a tired appearance. These lines are produced by repeated muscle contractions most noticeable on the forehead, between the eyebrows and around the eyes. Relaxa® relaxes these muscles to give the skin a smooth appearance.<br>(Relaxa®, Smoothel®, Calmora®)</p>
  </section>

  <section class="service svc-fillers">
    <h2>Dermal Fillers</h2>
    <p>Fibrin Growth Factor (FGF) facial treatment enhances skin rejuvenation, scar and wound rejuvenation, and hair restoration by injecting plasma rich fibrin into the face. This component of contains fibrin growth factors and proteins that enhance cellular healing, rejuvenate tone, and promote new collagen growth.</p>
  </section>

  <section class="service svc-fgf">
    <h2>Fibrin Growth Factor <small>(FGF)</small></h2>
    <p>Dermal filler treatments plump up smile and frown lines, thin lips, and decrease cheek wrinkles and chin folds with FDA-approved volumizing hyaluronic acid, thus allow skin to restore fullness from the inside out.<br>LIPS<br>SMILE LINES/NASOLABIAL FOLDS</p>
  </section>

  <section class="service svc-pen">
    <h2>DermaPoint®</h2>
    <p>DermaPoint® is a microneedling treatment that generates the skin's self-repair mechanism and activates collagen and elastin production. Microneedling is great for scarring, problems with texture, enlarged pores, and even stretch marks.</p>
  </section>

  <section class="service svc-peels">
    <h2>Chemical Peels</h2>
    <p>Chemical Peels improve skin texture correcting pigmentation concerns, sun damage, and scarring.</p>
  </section>
</main>
</body>
</html>
```